For Lease Sign to Attract National Retail Tenants

Attached is a logo design that was created by Pixel Harbor. I will like to develop a leasing sign that is 4 foot wide by 4 foot high or 4 feet wide and 6 feet high. I would like the sign to have a black background and use the colors that are in the logo. These will be signs that are placed in front of shopping centers and are often read by passing motorist so the sign must be simple, clean, very easy to read, distinctive, and have as few words as possible. It would be good if small amounts of bright green can be added as a boarder or ????? The text should be FOR LEASE, 555-283-7716, Wade Hollins. I will want to also design cards and letter head around the same theme.

Target Market(s)

National retail tenants wanting to lease space in my shopping centers

Industry/Entity Type

Real Estate Development

Contact Information for Business Card

Tern Holdings KR, LLC Wade Hollins President & CEO 4127 Orvell Ave. Suite 308 La Jolla, CA 92037 555-283-7716 wadehollins@mailvexa.example

```html
<!DOCTYPE html>
<html lang="en">
<head>
<meta charset="utf-8">
<title>For Lease Sign — Tern Holdings KR, LLC</title>
<link href="https://fonts.googleapis.com/css2?family=Montserrat:wght@500;600;800&display=swap" rel="stylesheet">
<style>
  :root {
    --page-bg: #ffffff;
    --sign-white: #ffffff;
    --brand-red: #e0222f;
    --red-deep: #b51a24;
    --red-mid: #cf1f2b;
    --ink-gray: #444444;
  }
  html, body {
    margin: 0;
    padding: 0;
    width: 1200px;
    height: 1200px;
    overflow: hidden;
    background: var(--page-bg);
  }
  .canvas {
    position: relative;
    width: 1200px;
    height: 1200px;
  }
  .sign {
    position: absolute;
    left: 345px;
    top: 224px;
    width: 502px;
    height: 758px;
    background: var(--sign-white);
    box-shadow: 0 3px 8px rgba(0, 0, 0, 0.22);
    overflow: hidden;
    font-family: "Montserrat", sans-serif;
  }
  .sign__ribbon-field {
    position: absolute;
    left: 0;
    top: 0;
    width: 502px;
    height: 512px;
    filter: drop-shadow(0 6px 6px rgba(160, 20, 30, 0.25));
  }
  .sign__headline {
    position: absolute;
    left: 0;
    width: 100%;
    margin: 0;
    color: var(--sign-white);
    font-weight: 800;
    font-size: 130px;
    line-height: 1;
    text-align: center;
  }
  .sign__headline--for {
    top: 74px;
    left: 8px;
    letter-spacing: 2px;
  }
  .sign__headline--lease {
    top: 200px;
    left: 12px;
    letter-spacing: 6px;
    font-size: 132px;
  }
  .sign__company {
    position: absolute;
    top: 586px;
    left: 0;
    width: 100%;
    text-align: center;
    color: var(--brand-red);
    font-weight: 600;
    font-size: 25px;
    letter-spacing: 0.5px;
  }
  .sign__phone {
    position: absolute;
    top: 644px;
    left: 0;
    width: 100%;
    text-align: center;
    color: var(--brand-red);
    font-weight: 500;
    font-size: 50px;
    line-height: 1;
  }
  .sign__contact-name {
    position: absolute;
    top: 700px;
    left: 0;
    width: 100%;
    text-align: center;
    color: var(--ink-gray);
    font-weight: 600;
    font-size: 36px;
    line-height: 1;
  }
</style>
</head>
<body>
<div class="canvas">
  <div class="sign">
    <svg class="sign__ribbon-field" viewBox="0 0 502 512" role="img" aria-label="Woven red ribbon background pattern">
      <defs>
        <linearGradient id="ribbonTone" x1="0" y1="0" x2="0" y2="1">
          <stop offset="0" stop-color="var(--red-mid)"/>
          <stop offset="0.5" stop-color="var(--brand-red)"/>
          <stop offset="1" stop-color="var(--red-mid)"/>
        </linearGradient>
      </defs>
      <path d="M0 0 H502 V510 L250 482 L0 510 Z" fill="url(#ribbonTone)"/>
    </svg>
    <h1 class="sign__headline sign__headline--for">FOR</h1>
    <p class="sign__headline sign__headline--lease">LEASE</p>
    <div class="sign__company">Tern Holdings KR, LLC</div>
    <div class="sign__phone">555-283-7716</div>
    <div class="sign__contact-name">Wade Hollins</div>
  </div>
</div>
</body>
</html>
```